New business Card Design

I'm looking to do a new design for our business cards.

Our Company its called the Lantern quarter we are a High end outdoor Design and construction company based out of miami FL

Our Style is elegant, minimalist, Luxury but accessible.

see our Website: www.thelanternquarter.example

Attached find our logo as well as some samples the cards that we have for our sister company.

Sample Contact information ( in no particular order):

Marco Bettancur
VP of Sales and Marketing
Marco@thelanternquarter.example
786.402.9158
4712 NW 63 AVE Miami Florida, 33166
Updates

Designs are Looking Great guys but not quite there yet!

Upload your last few designs between today and Tomorrow. we will be choosing one on Saturday!

Cheers, 

Marco Bettancur
Director Of Marketing 

Hello Guys, 

Sorry we have not made a decision yet.  a lot of cool stuff! just narrowing down our options. 
expect a decision with in a day or 2. 

Marco. 

Target Market(s)

high End Design and construction. Luxurious but accessible

Industry/Entity Type

Construction

Colors

Designer to choose colors to be used in the design.

```html
<!DOCTYPE html>
<html lang="en">
<head>
<meta charset="utf-8">
<title>The Lantern Quarter — Business Card</title>
<link href="https://fonts.googleapis.com/css2?family=Bebas+Neue&family=Open+Sans:wght@400;600&display=swap" rel="stylesheet">
<style>
  :root {
    --backdrop: #e9e7e4;
    --card: #fbfbfb;
    --brand-blue: #1c77c3;
    --ink: #3a3a3a;
    --muted: #555;
    --row: #ececec;
    --mark-green: #6fb43f;
    --faint: #dfe5ee;
  }
  * { box-sizing: border-box; margin: 0; padding: 0; }
  html, body { width: 1200px; height: 1080px; overflow: hidden; background: var(--backdrop); }
  .canvas { position: relative; width: 1200px; height: 1080px; }
  .card {
    position: absolute; top: 172px; width: 420px; height: 735px;
    background: var(--card); overflow: hidden;
    box-shadow: 0 10px 30px rgba(0,0,0,.18);
  }
  .card--front { left: 150px; }
  .card--back { left: 630px; }

  /* front */
  .side-band { position: absolute; left: 0; top: 0; width: 42px; height: 520px; background: var(--brand-blue); }
  .corner-block { position: absolute; left: 0; bottom: 0; width: 110px; height: 62px; background: var(--brand-blue); }
  .name-rule { position: absolute; left: 150px; right: 0; top: 118px; height: 8px; background: var(--brand-blue); }
  .name {
    position: absolute; left: 150px; top: 96px; padding: 6px 12px 2px;
    background: var(--brand-blue); color: #fff; white-space: nowrap;
    font: 34px/1 "Bebas Neue", sans-serif; letter-spacing: .5px;
  }
  .title { position: absolute; left: 170px; top: 140px; font: 13px "Open Sans", sans-serif; color: var(--muted); white-space: nowrap; }
  .company {
    position: absolute; left: 72px; top: 356px; white-space: nowrap;
    font: 42px/1 "Bebas Neue", sans-serif; color: var(--ink); letter-spacing: .5px;
  }
  .company .accent { color: var(--brand-blue); }
  .contact { position: absolute; left: 42px; right: 20px; top: 410px; list-style: none; }
  .contact li {
    display: flex; align-items: center; gap: 14px;
    height: 40px; margin-bottom: 6px; padding-left: 92px;
    background: var(--row); white-space: nowrap;
    font: 13.5px "Open Sans", sans-serif; color: var(--ink);
  }
  .contact li:first-child { margin-left: 30px; padding-left: 62px; }
  .contact .icon { width: 14px; height: 14px; flex: none; }
  .contact .plain { padding-left: 120px; }

  /* back */
  .mark { position: absolute; left: 0; right: 0; top: 200px; display: flex; justify-content: center; align-items: center; gap: 12px; }
  .mark-dot { width: 26px; height: 26px; border-radius: 50%; background: var(--mark-green); }
  .mark-name { font: 32px/1 "Bebas Neue", sans-serif; color: var(--brand-blue); letter-spacing: 1px; white-space: nowrap; }
  .back-band {
    position: absolute; left: 0; right: 0; top: 370px; height: 62px;
    background: var(--brand-blue); color: #fff; white-space: nowrap;
    font: 38px/62px "Bebas Neue", sans-serif; text-align: center; letter-spacing: .5px;
  }
  .web {
    position: absolute; left: 40px; right: 40px; top: 440px; height: 36px;
    background: var(--row); font: 13.5px/36px "Open Sans", sans-serif; color: var(--ink); text-align: center;
  }
  .faint-name {
    position: absolute; left: 0; right: 0; bottom: 40px; text-align: center; white-space: nowrap;
    font: 64px/1 "Bebas Neue", sans-serif; color: var(--faint);
  }
</style>
</head>
<body>
<main class="canvas">
  <section class="card card--front" aria-label="Card front">
    <div class="side-band"></div>
    <div class="corner-block"></div>
    <div class="name-rule"></div>
    <h1 class="name">Marco Bettancur</h1>
    <p class="title">VP of Sales and Marketing</p>
    <h2 class="company">The <span class="accent">Lantern</span> Quarter</h2>
    <ul class="contact">
      <li>
        <svg class="icon" viewBox="0 0 14 14"><path d="M7 1a4 4 0 0 0-4 4c0 3 4 8 4 8s4-5 4-8a4 4 0 0 0-4-4z" fill="var(--brand-blue)"/><circle cx="7" cy="5" r="1.5" fill="#fff"/></svg>
        4712 NW 63 AVE
      </li>
      <li class="plain">Miami Florida, 33166</li>
      <li>
        <svg class="icon" viewBox="0 0 14 14"><path d="M4 2h2l1 3-1.5 1a7 7 0 0 0 2.5 2.5L9 7l3 1v2a2 2 0 0 1-2 2C6 12 2 8 2 4a2 2 0 0 1 2-2z" fill="var(--brand-blue)"/></svg>
        786.402.9158
      </li>
      <li>
        <svg class="icon" viewBox="0 0 14 14"><rect x="1.5" y="3" width="11" height="8" fill="none" stroke="var(--brand-blue)" stroke-width="1.2"/><path d="M1.5 3 7 8l5.5-5" fill="none" stroke="var(--brand-blue)" stroke-width="1.2"/></svg>
        Marco@thelanternquarter.example
      </li>
    </ul>
  </section>

  <section class="card card--back" aria-label="Card back">
    <div class="mark"><span class="mark-dot"></span><span class="mark-name">The Lantern Quarter</span></div>
    <div class="back-band">The Lantern Quarter</div>
    <p class="web">www.thelanternquarter.example</p>
    <div class="faint-name">Lantern Quarter</div>
  </section>
</main>
</body>
</html>
```